FREE SOCIAL SECURITY DISABILITY CLAIM EVALUATION - Ad Banners & Email Marketing Creatives

Looking for design of ad banners and email creative for my Social Security Disability Insurance Benefits Application, Denial, & Appeals Help website. Call to action based email focused on conveying brand, messaging of "Are you out of work due to a disability? You may qualify for up to $2,642 per month in Social Security Disability benefits!" and "ACT NOW: Check Your Eligibility" Call to action of 'Get Your FREE Evaluation' or 'Fast, FREE, No Obligation Evaluation' or 'Confirm My Eligibility Now!' or 'Start My FREE Evaluation' or 'Confirm My Eligibility Now!'. Can use any messaging and images from the current website:
https://relief-filingdesk.com/

Please focus on imaging that matches the site. The final Ad Banners must be delivered in both JPG and PSD file formats. Ad Banners must follow OMC standards.

We need Ad Banners in the following sizes.
728x90
300x250
336x280
160x600
1200x628
600x600
1080x1080
Email

Target Market(s)
People in the US between the ages 48-63 looking for Social Security Disability Insurance Benefits Application, Denial, & Appeals Help. Get connected to a local Social Security Disability legal representative for a free, no-obligation evaluation. Find out if you are eligible to receive financial compensation for as much as $2,642 a month!

Should not be cookie cutter. Stick to simple yet official looking.

The final Email creative must be done in responsive HTML as well as text for easy use and include Email Opt Out link etc.

Target Market(s)

Americans that are between the ages 48-63 that have a physical condition that prevents them from working. Many times the physical condition is a result of an injury.

Coding

Coded - Design and coding required

Font styles to use
Sans Serif

Requirements
Must have
• A strong call to action.
Should not have
• No photos of people in wheelchairs.

```html
<!DOCTYPE html>
<html lang="en">
<head>
<meta charset="utf-8">
<title>Free Social Security Disability Claim Evaluation</title>
<link rel="stylesheet" href="https://fonts.googleapis.com/css2?family=Oswald:wght@300;400&family=Poppins:wght@300;400;500;600&family=Tinos:wght@700&display=swap">
<style>
  :root {
    --sky-bar: #8cc3e0;
    --navy: #13223f;
    --heading-navy: #16285a;
    --page-grey: #ececec;
    --white: #ffffff;
    --hero-blue-start: #00a3df;
    --hero-blue-end: #3dd5f1;
    --band-blue: #00a7e1;
    --cta-red: #ff0000;
    --body-grey: #777777;
    --accent-blue: #2fa6d6;
    --tile-blue: #2a5b93;
    --social-one: #4f73b5;
    --social-two: #6ecdf2;
    --social-three: #c8202e;
  }
  * { margin: 0; padding: 0; box-sizing: border-box; }
  html, body { width: 1200px; height: 2810px; overflow: hidden; }
  body {
    position: relative;
    background: var(--page-grey);
    font-family: "Poppins", Arial, sans-serif;
  }
  .browser-bar {
    position: absolute; left: 0; top: 0; width: 1200px; height: 92px;
    background: var(--sky-bar); color: var(--white);
    font-family: Arial, Helvetica, sans-serif; font-size: 26px;
    display: flex; align-items: center; justify-content: center;
  }
  .masthead {
    position: absolute; left: 0; top: 92px; width: 1200px; height: 233px;
    background: var(--navy);
  }
  .brand-mark { position: absolute; background: var(--sky-bar); }
  .masthead .brand-mark { left: 61px; top: 60px; width: 125px; height: 112px; }
  .brand-title {
    position: absolute; color: var(--white);
    font-family: "Oswald", "Arial Narrow", sans-serif; font-weight: 400;
    white-space: nowrap; letter-spacing: 0.09em;
    font-size: 37px;
  }
  .masthead .brand-title { left: 208px; top: 86px; width: 940px; line-height: 60px; }
  .content-column {
    position: absolute; left: 44px; top: 325px; width: 1105px; height: 1772px;
    background: var(--white);
  }
  .hero-card {
    position: absolute; left: 79px; top: 347px; width: 1033px; height: 585px;
    border-radius: 56px; background: var(--white);
    border: 2px solid #dcdcdc; box-shadow: 0 2px 8px rgba(0,0,0,0.12);
  }
  .hero-panel {
    position: absolute; left: 96px; top: 364px; width: 999px; height: 551px;
    border-radius: 42px;
    background: linear-gradient(90deg, var(--hero-blue-start) 0%, var(--hero-blue-start) 45%, var(--hero-blue-end) 100%);
  }
  .hero-copy {
    position: absolute; left: 130px; top: 457px; color: var(--white);
    font-family: "Poppins", Arial, sans-serif;
  }
  .hero-copy .lead { font-weight: 300; font-size: 43px; line-height: 50px; letter-spacing: 0.02em; }
  .hero-copy .headline { font-weight: 600; font-size: 58px; line-height: 63px; letter-spacing: 0.045em; margin-top: 8px; }
  .hero-art { position: absolute; left: 640px; top: 441px; width: 411px; height: 426px; }
  .cta-button {
    position: absolute; left: 202px; top: 957px; width: 772px; height: 114px;
    border-radius: 57px; background: var(--cta-red); color: var(--white);
    font-weight: 600; font-size: 40px; letter-spacing: 0.1em;
    display: flex; align-items: center; justify-content: center;
    text-decoration: none; white-space: nowrap;
  }
  .section-title {
    position: absolute; left: 44px; width: 1105px; top: 1148px;
    text-align: center; color: var(--heading-navy);
    font-weight: 500; font-size: 44px; line-height: 60px;
  }
  .body-copy {
    position: absolute; left: 92px; width: 1009px;
    text-align: center; color: var(--body-grey);
    font-weight: 300; font-size: 26.5px; line-height: 44px;
  }
  .body-copy.first { top: 1242px; }
  .body-copy.second { top: 1463px; }
  .free-band {
    position: absolute; left: 42px; top: 1762px; width: 1107px; height: 335px;
    background: var(--band-blue);
  }
  .free-frame {
    position: absolute; left: 73px; top: 1797px; width: 1046px; height: 267px;
    border: 5px solid var(--white);
    color: var(--white); text-align: center;
  }
  .free-frame .big {
    font-family: "Tinos", "Times New Roman", serif; font-weight: 700;
    font-size: 88px; line-height: 100px; margin-top: 38px;
  }
  .free-frame .small { font-weight: 500; font-size: 33px; line-height: 44px; margin-top: 6px; letter-spacing: 0.01em; }
  .site-footer {
    position: absolute; left: 0; top: 2097px; width: 1200px; height: 443px;
    background: var(--navy); color: var(--white); text-align: center;
  }
  .site-footer .brand-mark { left: 531px; top: 37px; width: 125px; height: 112px; }
  .site-footer .brand-title {
    left: 0; width: 1200px; top: 176px; line-height: 56px; text-align: center;
  }
  .contact-line {
    position: absolute; left: 0; width: 1200px; top: 283px;
    font-size: 28px; line-height: 40px; letter-spacing: 0.02em; white-space: nowrap;
  }
  .contact-line .label { color: var(--accent-blue); font-weight: 500; }
  .contact-line .sep { margin: 0 22px; }
  .site-link {
    position: absolute; left: 0; width: 1200px; top: 345px;
    font-size: 30px; line-height: 40px; font-weight: 500; letter-spacing: 0.04em;
  }
  .social-row { position: absolute; left: 448px; top: 2633px; width: 300px; height: 92px; }
</style>
</head>
<body>
  <div class="browser-bar">View in web browser</div>

  <header class="masthead">
    <div class="brand-mark" aria-hidden="true"></div>
    <div class="brand-title">FREE SOCIAL SECURITY DISABILITY CLAIM EVALUATION</div>
  </header>

  <main class="content-column"></main>

  <div class="hero-card"></div>
  <div class="hero-panel"></div>
  <div class="hero-copy">
    <div class="lead">Social Security<br>Disability Insurance<br>Benefits</div>
    <div class="headline">APPLICATION,<br>DENIAL, &amp;<br>APPEALS HELP.</div>
  </div>
  <svg class="hero-art" role="img" aria-label="Four blue tiles showing disability symbols: mobility, cognition, sign language and vision" viewBox="0 0 411 426">
    <rect x="0" y="0" width="200" height="196" rx="14" fill="var(--tile-blue)"/>
    <rect x="211" y="0" width="200" height="196" rx="14" fill="var(--tile-blue)"/>
    <rect x="0" y="228" width="200" height="198" rx="14" fill="var(--tile-blue)"/>
    <rect x="211" y="228" width="200" height="198" rx="14" fill="var(--tile-blue)"/>
  </svg>

  <a class="cta-button" href="https://relief-filingdesk.com/">CHECK YOUR ELIGIBITY NOW</a>

  <h2 class="section-title">How It Works?</h2>
  <p class="body-copy first">Utilizing a Social Security Disability attorney or advocate may improve your chances of initial approval, get your approval processed more quickly and in many cases increase the amount of benefits you are awarded. There are no upfront expenses to you for the evaluation, filing or appeal process.</p>
  <p class="body-copy second">To get immediate assistance from one of our attorneys or advocates, please fill out the FREE Evaluation Form Above. This website is not affiliated with the Social Security Administration ("SSA") or any state or federal agency. If you choose to apply on your own without representation, you may do so at no cost on the SSA website.</p>

  <div class="free-band"></div>
  <div class="free-frame">
    <div class="big">ITS FREE!</div>
    <div class="small">All you have to fill up the form- only take 30 seconds</div>
  </div>

  <footer class="site-footer">
    <div class="brand-mark" aria-hidden="true"></div>
    <div class="brand-title">FREE SOCIAL SECURITY DISABILITY CLAIM EVALUATION</div>
    <div class="contact-line">
      <span class="label">Phone:</span> 8888 .5550.0142<span class="sep">|</span><span class="label">Email:</span> info@relief-filingdesk.com
    </div>
    <div class="site-link">www.relief-filingdesk.com</div>
  </footer>

  <svg class="social-row" viewBox="0 0 300 92" role="img" aria-label="Social media links">
    <circle cx="46" cy="46" r="46" fill="var(--social-one)"/>
    <circle cx="147" cy="46" r="46" fill="var(--social-two)"/>
    <circle cx="247" cy="46" r="46" fill="var(--social-three)"/>
  </svg>
</body>
</html>
```